Tech business card design

We need an amazing business card design for our new business 'Vantry' a marketing tech startup based in Sydney, Australia. We provide an online marketplace for businesses to search and buy advertising media, connect with service providers and learn more about marketing. We wish to communicate 'cool tech', reliability and professionalism and design based around our logo.

Target Market(s)

Business Owners

Contact Information for Business Card

Name
Position
Email Address
Website
Phone Number

Font styles to use
Other font styles liked:
• Avenir & Avenir Next

Colors

Designer to choose colors to be used in the design.

```html
<!DOCTYPE html>
<html lang="en">
<head>
<meta charset="utf-8">
<title>Vantry Business Card</title>
<link href="https://fonts.googleapis.com/css2?family=Montserrat:wght@300;400;600;700;800&display=swap" rel="stylesheet">
<style>
  :root {
    --backdrop: #c6c6c6;
    --navy: #10113a;
    --paper: #ffffff;
    --ink: #16173f;
    --muted: #5a5b73;
    --rule: #9a9bb0;
    --rule-dark: #4a4c78;
    --web-dark: #9fa1c4;
  }
  * { margin: 0; padding: 0; box-sizing: border-box; }
  html, body {
    width: 1200px; height: 800px; overflow: hidden;
    background: var(--backdrop);
    font-family: "Montserrat", sans-serif;
  }
  .sheet {
    width: 1200px; height: 800px;
    display: flex; align-items: center; justify-content: center; gap: 50px;
  }
  .card {
    position: relative;
    width: 525px; height: 300px;
    border-radius: 34px;
    overflow: hidden;
    box-shadow: 0 10px 30px rgba(0,0,0,0.12);
  }
  /* Front: contact side */
  .card-front { background: var(--paper); color: var(--ink); }
  .brand-name {
    font-weight: 800; letter-spacing: -0.5px; line-height: 1;
  }
  .card-front .brand-name {
    position: absolute; left: 44px; top: 44px; font-size: 38px; color: var(--ink);
  }
  .person { position: absolute; left: 44px; top: 100px; }
  .person-name { font-weight: 700; font-size: 17px; }
  .person-title { font-weight: 300; font-size: 11px; color: var(--muted); margin-top: 3px; }
  .divider {
    position: absolute; left: 44px; top: 162px; width: 110px;
    border-top: 1px solid var(--rule);
  }
  .contacts {
    position: absolute; right: 40px; bottom: 42px;
    display: grid; grid-template-columns: auto auto; column-gap: 18px; row-gap: 6px;
    font-size: 10px;
  }
  .contact-label { font-weight: 700; }
  .contact-value { font-weight: 400; color: var(--muted); line-height: 1.45; }
  .contact-gap { height: 4px; grid-column: 1 / 3; }
  /* Back: brand side */
  .card-back { background: var(--navy); color: var(--paper); }
  .card-back .brand-name {
    position: absolute; left: 0; right: 0; top: 100px;
    text-align: center; font-size: 62px; color: var(--paper);
  }
  .footer-rule {
    position: absolute; left: 0; right: 0; top: 222px;
    display: flex; align-items: center; gap: 28px;
  }
  .footer-line { flex: 1; border-top: 1px solid var(--rule-dark); }
  .footer-web {
    font-size: 11px; font-weight: 300; letter-spacing: 1px; color: var(--web-dark);
    white-space: nowrap;
  }
</style>
</head>
<body>
<main class="sheet">
  <section class="card card-front" aria-label="Business card front">
    <div class="brand-name">vantry</div>
    <div class="person">
      <div class="person-name">Callum Reyes</div>
      <div class="person-title">Managing Director</div>
    </div>
    <div class="divider"></div>
    <div class="contacts">
      <span class="contact-label">Phone</span>
      <span class="contact-value">+61 (02) 8123 4470 (Fax)<br>+61 (04) 1175 3092 (Mobile)</span>
      <span class="contact-gap"></span>
      <span class="contact-label">E-Mail</span>
      <span class="contact-value">callum@vantry.co</span>
      <span class="contact-label">Website</span>
      <span class="contact-value">www.vantry.co</span>
      <span class="contact-label">Address</span>
      <span class="contact-value">89 Harbour Street, Sydney NSW 2000</span>
    </div>
  </section>

  <section class="card card-back" aria-label="Business card back">
    <div class="brand-name">vantry</div>
    <div class="footer-rule">
      <span class="footer-line"></span>
      <span class="footer-web">www.vantrymarketing.com</span>
      <span class="footer-line"></span>
    </div>
  </section>
</main>
</body>
</html>
```